Catering Brochure
tqsprouts.net
Project: Catering Brochure
Catering Brochure - Chef / Catering
Creative Brief
Chef / Catering
Families, children, fun, youthful
We require our logo to be in the brochure, sample food items from our website, our photos from our site (all of which we can provide)
tqsprouts tqsprouts
Thanks so much for the designs so far! We definitely like the look and feel of design #1 the best so far but we are looking to have a brochure that combines both of our businesses. We like the look of a photo film strip and really like the way the individual pictures were blended together. We need our contact info on the back of the brochure and also would like the logo colors to match- please match it to the pms color of the plain TQ logo please. Thanks for all of your hard work!
Font used is Optima
We have decided to combine our two logos and both parts of our business onto one tri-fold brochure. I have attached all of the content and the new logos to be added. Basically half should be devoted to Tolvane Quarry Catering and half to TQSprouts. We look forward to seeing your designs!
Hi. I forgot to specify that I would like a tri-fold brochure. Thanks!

```html
<!DOCTYPE html>
<html lang="en">
<head>
<meta charset="utf-8">
<title>TQSprouts &amp; Tolvane Quarry Catering – Tri-fold Brochure</title>
<link rel="stylesheet" href="https://fonts.googleapis.com/css2?family=Tenor+Sans&family=Lato:wght@400;700&display=swap">
<style>
  :root{
    --plum:#8a2a6c;
    --plum-deep:#5c1547;
    --plum-soft:#b0548f;
    --blush:#f4e3ee;
    --cream:#fbf6ef;
    --gold:#f2a72a;
    --ink:#3d2233;
    --white:#ffffff;
    --stage:#e9e4e6;
  }
  *{box-sizing:border-box;margin:0;padding:0}
  html,body{width:1200px;height:886px;overflow:hidden;background:var(--stage)}
  body{font-family:"Lato",sans-serif;color:var(--ink);position:relative}
  .spread{position:absolute;left:150px;width:900px;height:410px;display:flex;box-shadow:0 2px 8px rgba(0,0,0,.18);overflow:hidden}
  .spread--outside{top:22px}
  .spread--inside{top:454px;background:var(--white)}
  .panel{position:relative;width:300px;height:410px;overflow:hidden}
  .panel + .panel{border-left:1px solid rgba(0,0,0,.08)}
  .photo{position:absolute;display:block}
  .tag-bar{position:absolute;height:26px;display:flex;align-items:center;gap:8px;padding:0 12px;font-family:"Tenor Sans",sans-serif;font-size:14px;color:var(--white);background:var(--plum-deep)}
  .tag-bar--light{background:var(--white);color:var(--plum)}
  .dot{width:14px;height:14px;border-radius:50%;background:var(--gold);flex:none}
  .body-copy{position:absolute;font-size:9.5px;line-height:1.5;text-align:justify}
  .wordmark{font-family:"Tenor Sans",sans-serif;color:var(--plum);display:flex;align-items:center;gap:8px}
  .wordmark .mark-square{width:18px;height:18px;background:var(--plum);flex:none}

  /* outside */
  .back-flap{background:linear-gradient(180deg,var(--plum) 0%,var(--plum-deep) 100%);color:var(--white)}
  .back-flap .tag-bar{top:22px;left:0;width:190px;background:var(--white);color:var(--plum)}
  .back-flap .body-copy{top:62px;left:20px;width:260px;color:var(--white)}
  .contact{background:linear-gradient(180deg,var(--blush) 0%,var(--white) 70%)}
  .contact .photo--cookies{top:0;left:0;width:300px;height:150px;background:radial-gradient(circle at 40% 50%,#c98a4a 0%,#9c5a2b 55%,#e9d3b6 100%)}
  .contact .tag-bar{top:170px;right:0;width:170px;justify-content:flex-end}
  .contact .body-copy{top:210px;left:24px;width:252px;text-align:center}
  .contact-lines{position:absolute;top:262px;left:0;width:300px;text-align:center;font-size:10px;line-height:1.7;color:var(--plum-deep)}
  .contact .wordmark{position:absolute;bottom:30px;left:0;width:300px;justify-content:center;font-size:15px}
  .cover{background:linear-gradient(180deg,var(--white) 0%,var(--blush) 100%)}
  .cover .photo--bowl-top{top:0;right:0;width:170px;height:120px;background:radial-gradient(circle at 60% 40%,#f3e6a6 0%,#e2c56b 60%,#f7efd2 100%)}
  .cover .wordmark--kids{position:absolute;top:38px;left:22px;font-size:26px;flex-direction:column;align-items:flex-start;gap:2px}
  .cover .wordmark--kids .mark-circle{width:34px;height:34px;border-radius:50%;background:var(--plum)}
  .cover .photo--child{top:130px;left:0;width:300px;height:150px;background:linear-gradient(135deg,#d9c7b5 0%,#b89a80 50%,#8f6f59 100%)}
  .cover .bowls{position:absolute;top:258px;left:60px;display:flex;gap:16px}
  .cover .bowl{width:80px;height:80px;border-radius:50%;border:4px solid var(--white);box-shadow:0 1px 4px rgba(0,0,0,.2)}
  .cover .bowl--soup{background:radial-gradient(circle,#e9a93a 0%,#c4781b 100%)}
  .cover .bowl--stew{background:radial-gradient(circle,#e6c24a 0%,#9b8a2c 100%)}
  .cover .footer-band{position:absolute;bottom:0;left:0;width:300px;height:50px;background:var(--plum);display:flex;align-items:center;justify-content:center}
  .cover .footer-band .wordmark{color:var(--white);font-size:15px}
  .cover .footer-band .mark-square{background:var(--white)}

  /* inside */
  .inside-left{background:var(--white)}
  .inside-left .header-band{position:absolute;top:0;left:0;width:300px;height:40px;background:var(--plum);display:flex;align-items:center;padding-left:16px}
  .inside-left .header-band .wordmark{color:var(--white);font-size:17px;letter-spacing:1px}
  .inside-left .header-band .mark-square{background:var(--white)}
  .inside-left .photo--room{top:40px;left:0;width:300px;height:80px;background:linear-gradient(90deg,#6b4a3a 0%,#c9b39a 50%,#7a5a45 100%)}
  .inside-left .tag-bar{top:132px;left:0;width:180px}
  .inside-left .body-copy{top:168px;left:18px;width:264px}
  .inside-mid .body-copy{top:18px;left:18px;width:264px}
  .inside-right .tag-bar{top:14px;left:0;width:300px;background:var(--plum)}
  .service-list{position:absolute;top:50px;left:24px;list-style:none;font-size:10px;line-height:1.9;color:var(--plum-deep)}
  .service-list li::before{content:"";display:inline-block;width:6px;height:6px;border-radius:50%;background:var(--gold);margin-right:8px;vertical-align:middle}
  .banquet-band{position:absolute;left:0;top:250px;width:900px;height:160px;background:linear-gradient(90deg,#d9cfc6 0%,#f2ece6 40%,#e4d6d0 70%,#c7b3a8 100%)}
  .food-circles{position:absolute;top:200px;left:290px;display:flex;gap:14px;z-index:2}
  .food-circle{width:76px;height:76px;border-radius:50%;border:4px solid var(--white);box-shadow:0 1px 4px rgba(0,0,0,.25)}
  .food-circle--pasta{background:radial-gradient(circle,#d9a25a 0%,#8f5a2a 100%)}
  .food-circle--cupcakes{background:radial-gradient(circle,#c7e3f0 0%,#e8a7c4 100%)}
  .food-circle--salad{background:radial-gradient(circle,#9cc45a 0%,#b8522f 100%)}
  .food-circle--dessert{background:radial-gradient(circle,#f3e2cf 0%,#b67d52 100%)}
  .plum-rule{position:absolute;left:0;top:246px;width:900px;height:4px;background:var(--plum)}
</style>
</head>
<body>

<section class="spread spread--outside" aria-label="Brochure outside">
  <div class="panel back-flap">
    <div class="tag-bar"><span>TQSprouts</span><span class="dot"></span></div>
    <p class="body-copy">At TQSprouts, our goal is to serve healthy, freshly made meals that children love. Every dish is cooked each morning using seasonal produce, whole grains and lean proteins. We work with schools, daycares and family events to bring balanced menus to every table. Our menus change with the seasons so young eaters can discover new flavours while parents enjoy peace of mind.</p>
  </div>

  <div class="panel contact">
    <div class="photo photo--cookies" role="img" aria-label="Photo of freshly baked cookies"></div>
    <div class="tag-bar"><span>Contact Us</span><span class="dot"></span></div>
    <p class="body-copy">Children's menus and party platters available year round. Call us to plan your next school lunch program or family celebration.</p>
    <div class="contact-lines">
      hello@tqsprouts.net<br>
      (555) 014-2276<br>
      www.tqsprouts.net
    </div>
    <div class="wordmark"><span class="mark-square"></span><span>Tolvane Quarry Catering</span></div>
  </div>

  <div class="panel cover">
    <div class="photo photo--bowl-top" role="img" aria-label="Photo of a bowl of pasta"></div>
    <div class="wordmark wordmark--kids"><span class="mark-circle"></span><span>TQ KIDS</span></div>
    <div class="photo photo--child" role="img" aria-label="Photo of a child enjoying a meal"></div>
    <div class="bowls">
      <div class="bowl bowl--soup" role="img" aria-label="Photo of a bowl of soup"></div>
      <div class="bowl bowl--stew" role="img" aria-label="Photo of a bowl of vegetable stew"></div>
    </div>
    <div class="footer-band"><div class="wordmark"><span class="mark-square"></span><span>Tolvane Quarry Catering</span></div></div>
  </div>
</section>

<section class="spread spread--inside" aria-label="Brochure inside">
  <div class="banquet-band" role="img" aria-label="Photo of a banquet hall set for a reception"></div>
  <div class="plum-rule"></div>

  <div class="panel inside-left">
    <div class="header-band"><div class="wordmark"><span class="mark-square"></span><span>TOLVANE QUARRY</span></div></div>
    <div class="photo photo--room" role="img" aria-label="Photo of the catering venue entrance"></div>
    <div class="tag-bar"><span>TQ Catering</span><span class="dot"></span></div>
    <p class="body-copy">Tolvane Quarry Catering has been providing culinary excellence throughout the region for over fifteen years. From intimate dinners to grand weddings, our chefs design each menu around your guests, your venue and your budget.</p>
  </div>

  <div class="panel inside-mid">
    <p class="body-copy">Every event begins with a conversation. We listen, taste and plan with you until the menu feels right. Our dedicated staff handle setup, service and cleanup so you can simply enjoy the day with the people who matter most.</p>
  </div>

  <div class="panel inside-right">
    <div class="tag-bar"><span>Services Include</span><span class="dot"></span></div>
    <ul class="service-list">
      <li>Weddings and receptions</li>
      <li>Corporate lunches</li>
      <li>Birthday parties</li>
      <li>School meal programs</li>
      <li>Holiday gatherings</li>
      <li>Private chef dinners</li>
      <li>Dessert and pastry tables</li>
    </ul>
  </div>

  <div class="food-circles">
    <div class="food-circle food-circle--pasta" role="img" aria-label="Photo of a pasta dish"></div>
    <div class="food-circle food-circle--cupcakes" role="img" aria-label="Photo of decorated cupcakes"></div>
    <div class="food-circle food-circle--salad" role="img" aria-label="Photo of a fresh salad"></div>
    <div class="food-circle food-circle--dessert" role="img" aria-label="Photo of a plated dessert"></div>
  </div>
</section>

</body>
</html>
```